KT Sentry 'Welcome' Envelope

I am looking for a 'Welcome' envelope design for new customers who sign up for our Alarm Services. In this envelope we will send confidential documents that the customer will need. I want it to stand out, yet look classy.

```html
<!DOCTYPE html>
<html lang="en">
<head>
<meta charset="utf-8">
<title>KT Sentry Welcome Envelope</title>
<link href="https://fonts.googleapis.com/css2?family=Poppins:wght@300;400;700&display=swap" rel="stylesheet">
<style>
:root{
  --board:#b3b3b3;
  --label:#6f6f6f;
  --env-deep:#05121a;
  --env-mid:#0b2d3c;
  --env-teal:#104a5f;
  --band:#0e3b4c;
  --flap:#0a3140;
  --lens-hi:#2fa8d8;
  --lens-lo:#0a3f7a;
  --green:#4cc03a;
  --white:#ffffff;
  --pale:#d9dee2;
  --faint:rgba(255,255,255,0.07);
}
*{margin:0;padding:0;box-sizing:border-box}
html,body{width:806px;height:1200px;overflow:hidden;background:var(--board);font-family:"Poppins",sans-serif}
.board{position:relative;width:806px;height:1200px}
.view-label{position:absolute;font-weight:300;font-size:20px;color:var(--label);letter-spacing:.5px}
.envelope{position:absolute;width:688px;height:296px;overflow:hidden;
  background:linear-gradient(180deg,var(--env-deep) 0 10px,transparent 10px),
  radial-gradient(ellipse 320px 220px at 345px 150px,var(--env-teal),var(--env-mid) 55%,var(--env-deep) 100%)}
.artwork{position:absolute;inset:0}
.lens{position:absolute;left:290px;top:100px;width:112px;height:112px;border-radius:50%;
  background:radial-gradient(circle at 45% 45%,var(--lens-hi),var(--lens-lo) 55%,#0b2231 72%,#3c5866 78%,#0b2231 84%);}
.band{position:absolute;left:0;right:0;top:228px;height:30px;background:var(--band)}
.stripes{position:absolute;left:0;right:0;top:258px;height:36px;
  background:repeating-linear-gradient(180deg,rgba(255,255,255,.12) 0 1px,transparent 1px 5px)}
.seal{position:absolute;width:130px;height:130px;border-radius:16px;transform:rotate(45deg);
  background:var(--faint);border:1px solid rgba(255,255,255,.08)}
.brand{position:absolute;left:24px;top:36px;font-weight:700;font-size:28px;color:var(--green);line-height:1}
.contact{position:absolute;left:27px;color:var(--white)}
.contact svg{position:absolute;left:0}
.address{top:76px}
.address p{padding-left:21px;font-size:11px;line-height:13px}
.phone{top:148px}
.phone p{padding-left:23px;font-size:16px}
.hours{top:172px}
.hours p{padding-left:23px;font-size:11px}
.window{position:absolute;left:24px;top:200px;width:210px;height:73px;background:var(--white);border-radius:9px}
.title{position:absolute;right:12px;top:224px;font-weight:300;font-size:28px;color:var(--pale);letter-spacing:.5px}
.bold .contact p{font-weight:700}
.light .contact p{font-weight:300}
.light .address p{font-size:12px;line-height:18px}
.light .phone p{font-size:13px}
.light .hours p{font-size:12px}
.flap{position:absolute;left:0;top:0}
.back-brand{position:absolute;left:0;right:0;top:216px;text-align:center;font-weight:700;font-size:24px;color:var(--green);line-height:1}
.tagline{position:absolute;left:0;right:0;top:252px;text-align:center;font-weight:400;font-size:13px;color:var(--white)}
</style>
</head>
<body>
<main class="board">

  <h2 class="view-label" style="left:42px;top:26px">FRONT 1</h2>
  <section class="envelope bold" style="left:57px;top:92px">
    <div class="artwork" role="img" aria-label="Camera shutter and lens illustration in deep teal tones"></div>
    <div class="band"></div><div class="stripes"></div>
    <div class="lens" role="img" aria-label="Security camera lens"></div>
    <div class="seal" style="left:460px;top:38px"></div>
    <div class="brand">KT Sentry</div>
    <div class="contact address">
      <svg width="12" height="18" viewBox="0 0 12 18"><path d="M6 0a6 6 0 0 0-6 6c0 4.5 6 12 6 12s6-7.5 6-12a6 6 0 0 0-6-6zm0 8.5A2.5 2.5 0 1 1 6 3.5a2.5 2.5 0 0 1 0 5z" fill="#ccd3d8"/></svg>
      <p>PO Box 482605</p><p>Tucson, AZ 85702</p>
    </div>
    <div class="contact phone">
      <svg width="14" height="14" viewBox="0 0 14 14" style="top:4px"><rect width="14" height="14" rx="3" fill="#ccd3d8"/><path d="M4 3l2 2-1 1.3a6 6 0 0 0 2.7 2.7L9 8l2 2-1.3 1.5C6.5 11 3 7.5 2.5 4.3z" fill="#0b2d3c"/></svg>
      <p>888 - 555 - 0142</p>
    </div>
    <div class="contact hours">
      <svg width="15" height="15" viewBox="0 0 16 16" style="top:-1px"><path d="M3 8a5 5 0 1 0 1.5-3.5M3 2v3h3" fill="none" stroke="#ccd3d8" stroke-width="1.8"/><path d="M8 5v3.5l2 1" fill="none" stroke="#ccd3d8" stroke-width="1.6"/></svg>
      <p>24 HOUR PROTECTION</p>
    </div>
    <div class="window"></div>
    <div class="title">WELCOME LETTER</div>
  </section>

  <h2 class="view-label" style="left:48px;top:448px">FRONT2</h2>
  <section class="envelope light" style="left:49px;top:488px">
    <div class="artwork" role="img" aria-label="Camera shutter and lens illustration in deep teal tones"></div>
    <div class="band"></div><div class="stripes"></div>
    <div class="lens" role="img" aria-label="Security camera lens"></div>
    <div class="seal" style="left:460px;top:38px"></div>
    <div class="brand">KT Sentry</div>
    <div class="contact address" style="left:24px">
      <svg width="12" height="18" viewBox="0 0 12 18" style="top:2px"><path d="M6 0a6 6 0 0 0-6 6c0 4.5 6 12 6 12s6-7.5 6-12a6 6 0 0 0-6-6zm0 8.5A2.5 2.5 0 1 1 6 3.5a2.5 2.5 0 0 1 0 5z" fill="#1f7fc0"/></svg>
      <p>PO Box 482605</p><p>Tucson, AZ 85702</p>
    </div>
    <div class="contact phone" style="left:24px;top:146px">
      <svg width="14" height="14" viewBox="0 0 14 14" style="top:3px"><rect width="14" height="14" rx="3" fill="#1f7fc0"/><path d="M4 3l2 2-1 1.3a6 6 0 0 0 2.7 2.7L9 8l2 2-1.3 1.5C6.5 11 3 7.5 2.5 4.3z" fill="#0b2d3c"/></svg>
      <p>888 . 555 . 0142</p>
    </div>
    <div class="contact hours" style="left:24px;top:168px">
      <svg width="15" height="15" viewBox="0 0 16 16" style="top:1px"><path d="M3 8a5 5 0 1 0 1.5-3.5M3 2v3h3" fill="none" stroke="#1f7fc0" stroke-width="1.8"/><path d="M8 5v3.5l2 1" fill="none" stroke="#1f7fc0" stroke-width="1.6"/></svg>
      <p>24 HOUR PROTECTION</p>
    </div>
    <div class="window"></div>
    <div class="title">WELCOME LETTER</div>
  </section>

  <h2 class="view-label" style="left:56px;top:824px">BACK</h2>
  <section class="envelope" style="left:57px;top:860px">
    <div class="artwork" role="img" aria-label="Camera shutter and lens illustration in deep teal tones"></div>
    <svg class="flap" width="688" height="48" viewBox="0 0 688 48"><polygon points="8,6 680,6 654,46 34,46" fill="var(--flap)"/></svg>
    <div class="band" style="top:218px"></div>
    <div class="lens" role="img" aria-label="Security camera lens" style="top:94px"></div>
    <div class="seal" style="left:20px;top:110px;width:105px;height:105px"></div>
    <div class="seal" style="left:520px;top:150px"></div>
    <div class="back-brand">KT Sentry</div>
    <div class="tagline">SECURITY PRODUCTS DEALER</div>
  </section>

</main>
</body>
</html>
```